SilverLedgerOak - Double Sided Business Card

We are looking for design options or our business cards. We are a Business Solutions and HR solutions Provider - the theme is business, for this card.

Our brand colours are represented within our logo.

Details needed to be put on the front of the business card are:

Employees name: [Sample Name]
Role: [Sample Role]

Address: Suite 4 - Level 3/48 Halloran Avenue Kellerton NSW 2198
M: 0000 000 000
P: 1300 847 213
F: 1300 847 286
E: sample@silverledgeroak.com.au
www.silverledgeroak.com.au
Updates

Reason: Hello, could we please increase our deadline by 5 days. Thanking you, Tess

Target Market(s)

Business Owners, also Candidates looking for Employment

Industry/Entity Type

Business

Contact Information for Business Card

Role: [Sample Role]

M: 0000 000 000
P: 1300 847 213
F: 1300 847 286

Font styles to use
Sans Serif

Colors
3276b5
3176b5
0455a3
85abd2
cfdeed
ffffff
000000
1b1b1b
757575

Requirements
Must have
• Details needed to be put on the front of the business card are:
• Employees name: [Sample Name]
• Role: [Sample Role]
• Address: Suite 4 - Level 3/48 Halloran Avenue Kellerton NSW 2198
• M: 0000 000 000
• P: 1300 847 213
• F: 1300 847 286
• E: sample@silverledgeroak.com.au
• www.silverledgeroak.com.au
Nice to have
• Simplicity, clean and professional.

```html
<!DOCTYPE html>
<html lang="en">
<head>
<meta charset="utf-8">
<title>SilverLedgerOak – Business Card</title>
<link rel="stylesheet" href="https://fonts.googleapis.com/css2?family=Arimo:wght@400;700&display=swap">
<style>
  :root {
    --navy: #0f2d57;
    --brand-blue: #0455a3;
    --bright-blue: #1f74c4;
    --soft-blue: #85abd2;
    --ink: #1b1b1b;
    --grey: #757575;
    --paper: #ffffff;
    --backdrop: #d9d9d9;
  }
  * { box-sizing: border-box; margin: 0; padding: 0; }
  html, body {
    width: 1200px; height: 800px; overflow: hidden;
    background: var(--backdrop);
    font-family: "Arimo", Arial, sans-serif;
    color: var(--ink);
  }
  .sheet {
    position: relative; width: 1200px; height: 800px;
    display: flex; gap: 40px; align-items: center; justify-content: center;
  }
  .card {
    position: relative; width: 540px; height: 309px;
    background: var(--paper);
    box-shadow: 0 6px 18px rgba(0,0,0,.18);
    overflow: hidden;
  }
  .band {
    position: absolute; left: 0; right: 0; bottom: 0; height: 58px;
    background: var(--navy);
    border-bottom: 16px solid var(--bright-blue);
    display: flex; flex-direction: column; justify-content: center;
    padding: 0 26px; color: var(--paper);
  }
  .brand { display: flex; align-items: center; gap: 10px; }
  .brand-square { width: 26px; height: 26px; background: var(--navy); flex: none; }
  .brand-name {
    font-weight: 700; color: var(--brand-blue);
    font-size: 30px; letter-spacing: .5px; white-space: nowrap;
  }
  .brand-rule { height: 1px; background: var(--navy); margin: 8px 0 6px; }
  .tagline { font-size: 9.5px; font-weight: 700; color: var(--ink); white-space: nowrap; }

  /* front */
  .card-front .brand-block { position: absolute; left: 30px; top: 118px; width: 262px; }
  .card-front .brand-name { font-size: 24px; }
  .card-front .brand-square { width: 22px; height: 22px; }
  .person { position: absolute; right: 30px; top: 30px; text-align: right; }
  .person-name { font-size: 15px; font-weight: 700; }
  .person-role { font-size: 12px; font-weight: 700; color: var(--bright-blue); margin-top: 2px; }
  .contact {
    position: absolute; left: 315px; top: 98px; width: 205px;
    font-size: 10.5px; line-height: 1.45; list-style: none;
  }
  .card-front .band { align-items: flex-end; }
  .band-line { font-size: 12px; font-weight: 700; letter-spacing: .5px; }

  /* back */
  .card-back .brand-block { position: absolute; left: 60px; top: 78px; width: 420px; }
  .card-back .brand-name { font-size: 38px; }
  .card-back .brand-square { width: 34px; height: 34px; }
  .card-back .band { height: 66px; }
  .web { font-size: 22px; font-weight: 700; letter-spacing: .5px; }
  .web-tag { font-size: 10px; font-weight: 700; color: var(--soft-blue); margin-top: 2px; }
</style>
</head>
<body>
<main class="sheet">
  <section class="card card-front" aria-label="Business card front">
    <div class="brand-block">
      <div class="brand">
        <span class="brand-square"></span>
        <span class="brand-name">SilverLedgerOak</span>
      </div>
      <div class="brand-rule"></div>
      <p class="tagline">Helping small to medium business realise their potential</p>
    </div>
    <div class="person">
      <p class="person-name">Sample Name</p>
      <p class="person-role">ROLE</p>
    </div>
    <ul class="contact">
      <li>Suite 4 - Level 3/48 Halloran Avenue</li>
      <li>Kellerton NSW 2198</li>
      <li>Mobile: 0000 000 000</li>
      <li>Phone: 1300 847 213</li>
      <li>Fax: 1300 847 286</li>
      <li>sample@silverledgeroak.com.au</li>
      <li>www.silverledgeroak.com.au</li>
    </ul>
    <div class="band">
      <p class="band-line">Business Solutions and HR solutions Provider</p>
    </div>
  </section>

  <section class="card card-back" aria-label="Business card back">
    <div class="brand-block">
      <div class="brand">
        <span class="brand-square"></span>
        <span class="brand-name">SilverLedgerOak</span>
      </div>
      <div class="brand-rule"></div>
    </div>
    <div class="band">
      <p class="web">www.silverledgeroak.com.au</p>
      <p class="web-tag">Helping small to medium business realise their potential</p>
    </div>
  </section>
</main>
</body>
</html>
```